Small Business Consulting Firm Needs Business Card Design

Need a sleek modern business card with 2 sides matching the colors of our logo. We will be placing these with a mailer we are sending out. These business cards will only ever be given to business owners. We operate helping businesses who are struggling with cash flow or finances. If the green and blue design needs to be moved to the right of "Harborline Crest Consulting" for aesthetic purposes that is ok. We will need an editable file if possible. We would like to include the reps name, email, website, and phone number. For now just use Peter Vance, pvance@harborlinecrest.com, www.harborlinecrest.com, and 833-555-0172.

```html
<!DOCTYPE html>
<html lang="en">
<head>
<meta charset="utf-8">
<title>Harborline Crest Consulting – Business Card</title>
<link rel="stylesheet" href="https://fonts.googleapis.com/css2?family=Open+Sans:wght@400;600&family=Roboto:wght@400;500;700&display=swap">
<style>
  :root {
    --backdrop: #5f686e;
    --card: #ffffff;
    --ink: #3b3b3b;
    --text-dark: #222222;
    --brand-blue: #0a7fc6;
    --brand-green: #79b940;
    --green-fold: #4e8a22;
    --white: #ffffff;
  }
  * { box-sizing: border-box; margin: 0; padding: 0; }
  html, body {
    width: 1200px; height: 900px; overflow: hidden;
    background: var(--backdrop);
    font-family: "Roboto", Arial, sans-serif;
  }
  .sheet {
    position: relative; width: 1200px; height: 900px;
    display: flex; flex-direction: column; align-items: center; justify-content: center;
    gap: 44px;
  }
  .card {
    position: relative; width: 600px; height: 343px;
    background: var(--card); border-radius: 16px; overflow: hidden;
    box-shadow: 0 10px 24px rgba(0,0,0,0.35);
  }

  /* Front */
  .card-front { display: flex; align-items: center; justify-content: center; }
  .wordmark {
    font-family: "Open Sans", Arial, sans-serif; font-weight: 400; color: var(--ink);
    text-align: center; text-transform: uppercase; line-height: 1;
  }
  .wordmark-name { display: block; font-size: 44px; letter-spacing: 2px; }
  .wordmark-sub { display: block; font-size: 20px; letter-spacing: 14px; margin-top: 12px; padding-left: 14px; }

  /* Back */
  .blue-panel {
    position: absolute; top: 0; right: 0; width: 300px; height: 100%;
    background: var(--brand-blue);
  }
  .name-ribbon {
    position: absolute; top: 46px; left: 250px; width: 290px; height: 58px;
    background: var(--brand-green); color: var(--white);
    display: flex; flex-direction: column; justify-content: center; padding-left: 70px;
  }
  .ribbon-fold { position: absolute; top: 104px; left: 250px; }
  .rep-name { font-size: 20px; font-weight: 700; letter-spacing: 0.3px; }
  .rep-title { font-size: 11px; margin-top: 3px; }

  .back-logo { position: absolute; top: 92px; left: 40px; }
  .back-logo .wordmark-name { font-size: 25px; letter-spacing: 1px; text-align: left; }
  .back-logo .wordmark-sub { font-size: 11px; letter-spacing: 9px; margin-top: 7px; padding-left: 0; text-align: left; }
  .logo-square { width: 40px; height: 40px; background: var(--brand-green); margin-bottom: 14px; }

  .contact-list { position: absolute; left: 40px; bottom: 36px; list-style: none; }
  .contact-item { display: flex; align-items: center; gap: 12px; font-size: 14px; color: var(--text-dark); height: 26px; }
  .contact-icon {
    width: 20px; height: 20px; background: var(--brand-green);
    display: flex; align-items: center; justify-content: center;
  }

  .address {
    position: absolute; right: 30px; bottom: 46px; width: 240px;
    color: var(--white); font-size: 14px; line-height: 1.45; text-align: center;
  }
  .address svg { display: block; margin: 0 auto 8px; }
</style>
</head>
<body>
<main class="sheet">

  <section class="card card-front" aria-label="Card front">
    <div class="wordmark">
      <span class="wordmark-name">Harborline Crest</span>
      <span class="wordmark-sub">Consulting</span>
    </div>
  </section>

  <section class="card card-back" aria-label="Card back">
    <div class="blue-panel"></div>

    <svg class="ribbon-fold" width="40" height="22" viewBox="0 0 40 22" aria-hidden="true">
      <polygon points="0,0 40,0 40,22" fill="var(--green-fold)"/>
    </svg>
    <div class="name-ribbon">
      <span class="rep-name">PETER VANCE</span>
      <span class="rep-title">Founder &amp; Director</span>
    </div>

    <div class="back-logo">
      <div class="logo-square"></div>
      <div class="wordmark">
        <span class="wordmark-name">Harborline Crest</span>
        <span class="wordmark-sub">Consulting</span>
      </div>
    </div>

    <ul class="contact-list">
      <li class="contact-item">
        <span class="contact-icon"><svg width="12" height="12" viewBox="0 0 24 24"><path fill="#fff" d="M6.6 10.8a15 15 0 0 0 6.6 6.6l2.2-2.2a1 1 0 0 1 1-.25 11.4 11.4 0 0 0 3.6.57 1 1 0 0 1 1 1V20a1 1 0 0 1-1 1A17 17 0 0 1 3 4a1 1 0 0 1 1-1h3.5a1 1 0 0 1 1 1c0 1.25.2 2.45.57 3.57a1 1 0 0 1-.25 1z"/></svg></span>
        833-555-0172
      </li>
      <li class="contact-item">
        <span class="contact-icon"><svg width="12" height="12" viewBox="0 0 24 24"><path fill="#fff" d="M2 8c0-2 4-4 10-4s10 2 10 4v2h-5V8H7v2H2zM5 12h14l2 8H3zm7 2a2.5 2.5 0 1 0 0 5 2.5 2.5 0 0 0 0-5z"/></svg></span>
        833-555-0190
      </li>
      <li class="contact-item">
        <span class="contact-icon"><svg width="12" height="12" viewBox="0 0 24 24"><path fill="#fff" d="M2 5h20v14H2zm2 2v.5l8 5 8-5V7z"/></svg></span>
        pvance@harborlinecrest.com
      </li>
      <li class="contact-item">
        <span class="contact-icon"><svg width="12" height="12" viewBox="0 0 24 24"><g fill="none" stroke="#fff" stroke-width="2"><circle cx="12" cy="12" r="9"/><path d="M3 12h18M12 3c3 3 3 15 0 18M12 3c-3 3-3 15 0 18"/></g></svg></span>
        www.harborlinecrest.com
      </li>
    </ul>

    <div class="address">
      <svg width="14" height="18" viewBox="0 0 24 32" aria-hidden="true"><path fill="#fff" d="M12 0a11 11 0 0 0-11 11c0 8 11 21 11 21s11-13 11-21A11 11 0 0 0 12 0zm0 15a4 4 0 1 1 0-8 4 4 0 0 1 0 8z"/></svg>
      210 Marlow Street - Linden Vale<br>New Jersey 07288
    </div>
  </section>

</main>
</body>
</html>
```